Company or website name
- www.brambletonhiregroup.example
- Links to the website
- Brambleton Hire Group
- Describe your company and organization and target audience
- We are a full service executive recruiting and staffing company. We work within all vertical markets within the US.
- The design should have the following
- Please ensure to include colors of the logo but feel free to include other colors as well to enhance the brochure. I'm looking for a single 8.5 x 11 inch brochure with front and back. The back will have more specific information while the front will be more a space for photos and general information on our company.
- Other Facts

```html
<!DOCTYPE html>
<html lang="en">
<head>
<meta charset="UTF-8">
<title>Brambleton Hire Group – Brochure Front and Back</title>
<link href="https://fonts.googleapis.com/css2?family=Archivo+Black&family=Open+Sans:wght@400;600;700&family=Roboto:wght@700&display=swap" rel="stylesheet">
<style>
  :root {
    --backdrop: #d9dadc;
    --paper: #ffffff;
    --teal: #3b7d91;
    --teal-deep: #336f82;
    --charcoal: #2a2c31;
    --butter: #f4e88e;
    --ink-light: #ffffff;
    --ink-dark: #3a3d42;
    --brand-blue: #1f4f86;
    --photo-light: #e9e7e4;
    --photo-mid: #b9b3ac;
    --photo-dark: #3a3633;
  }
  * { margin: 0; padding: 0; box-sizing: border-box; }
  html, body {
    width: 875px;
    height: 1200px;
    overflow: hidden;
    background: var(--backdrop);
  }
  .spread {
    position: relative;
    width: 875px;
    height: 1200px;
    font-family: "Open Sans", Arial, sans-serif;
  }
  .page {
    position: absolute;
    top: 328px;
    width: 420px;
    height: 544px;
    background: var(--paper);
    overflow: hidden;
    box-shadow: 0 2px 10px rgba(0, 0, 0, 0.18);
  }
  .page--front { left: 12px; }
  .page--back { left: 443px; }

  /* ---------- Front ---------- */
  .brand-tag {
    position: absolute;
    top: 34px;
    left: 42px;
    height: 46px;
    display: flex;
    align-items: center;
    gap: 9px;
    padding: 0 10px;
    background: var(--paper);
  }
  .brand-mark {
    width: 26px;
    height: 26px;
    border-radius: 50%;
    background: var(--brand-blue);
    flex-shrink: 0;
  }
  .brand-name {
    font-weight: 600;
    font-size: 13px;
    white-space: nowrap;
    color: var(--brand-blue);
  }
  .team-photo {
    position: absolute;
    top: 88px;
    left: 0;
    width: 420px;
    height: 264px;
    background:
      radial-gradient(ellipse at 45% 45%, var(--photo-light) 0%, transparent 55%),
      linear-gradient(100deg, var(--photo-light) 0%, var(--photo-mid) 45%, var(--photo-dark) 100%);
  }
  .accent-band {
    position: absolute;
    left: 0;
    width: 420px;
    height: 16px;
    background: var(--charcoal);
  }
  .page--front .accent-band { top: 352px; }
  .message-panel {
    position: absolute;
    top: 368px;
    left: 0;
    width: 420px;
    height: 158px;
    background: linear-gradient(180deg, var(--teal) 0%, var(--teal-deep) 100%);
    color: var(--ink-light);
  }
  .tagline-lead {
    position: absolute;
    top: 14px;
    left: 120px;
    font-family: "Roboto", Arial, sans-serif;
    font-weight: 700;
    font-size: 19px;
    letter-spacing: -0.3px;
    white-space: nowrap;
  }
  .tagline-hero {
    position: absolute;
    top: 38px;
    left: 100px;
    font-family: "Archivo Black", "Arial Black", sans-serif;
    font-weight: 400;
    font-size: 37px;
    line-height: 1;
    letter-spacing: -1.2px;
    white-space: nowrap;
    color: var(--butter);
  }
  .mission-copy {
    position: absolute;
    top: 86px;
    left: 14px;
    right: 14px;
    font-size: 7.4px;
    line-height: 1.45;
  }
  .footer-rule {
    position: absolute;
    top: 130px;
    left: 42px;
    width: 336px;
    height: 1px;
    background: var(--butter);
  }
  .site-link {
    position: absolute;
    top: 137px;
    right: 16px;
    font-weight: 700;
    font-size: 10px;
    color: var(--butter);
    text-decoration: none;
  }

  /* ---------- Back ---------- */
  .column-bar {
    position: absolute;
    top: 44px;
    height: 24px;
    background: var(--teal);
  }
  .column-bar--left { left: 0; width: 196px; }
  .column-bar--right {
    left: 214px;
    width: 186px;
    display: flex;
    align-items: center;
    padding-left: 12px;
  }
  .section-title {
    font-weight: 700;
    font-size: 12px;
    letter-spacing: 0.4px;
    text-transform: uppercase;
    color: var(--ink-light);
  }
  .text-column {
    position: absolute;
    top: 80px;
    width: 180px;
    color: var(--ink-dark);
  }
  .text-column--left { left: 16px; }
  .text-column--right { left: 214px; }
  .column-subhead {
    font-weight: 700;
    font-size: 7.6px;
    letter-spacing: 0.3px;
    text-transform: uppercase;
    margin-bottom: 5px;
  }
  .column-copy {
    font-size: 7.6px;
    line-height: 1.6;
    text-align: justify;
    margin-bottom: 7px;
  }
  .page--back .accent-band { top: 360px; }
  .contact-panel {
    position: absolute;
    top: 376px;
    left: 0;
    width: 420px;
    height: 150px;
    background: linear-gradient(180deg, var(--teal) 0%, var(--teal-deep) 100%);
    color: var(--ink-light);
  }
  .contact-list {
    position: absolute;
    top: 30px;
    right: 20px;
    list-style: none;
    text-align: right;
    font-size: 10px;
    line-height: 2.1;
  }
  .contact-list a { color: var(--ink-light); text-decoration: none; }
</style>
</head>
<body>
  <div class="spread">
    <main class="page page--front">
      <div class="brand-tag">
        <span class="brand-mark"></span>
        <span class="brand-name">Brambleton Hire Group</span>
      </div>

      <div class="team-photo" role="img" aria-label="Photo of three smiling colleagues in business attire gathered around a computer monitor in a bright office"></div>

      <div class="accent-band"></div>

      <section class="message-panel">
        <p class="tagline-lead">Whatever you're looking for</p>
        <h1 class="tagline-hero">we've got it</h1>
        <p class="mission-copy">At Brambleton Hire Group, our mission is to match employers with employees to form successful work relationships. We succeed in our mission by providing excellent service to our clients and candidates, consistently meeting established expectations, and setting and maintaining the highest standards and ethics demonstrated in the employment services industry.</p>
        <div class="footer-rule"></div>
        <a class="site-link" href="https://www.brambletonhiregroup.example">www.brambletonhiregroup.example</a>
      </section>
    </main>

    <section class="page page--back">
      <div class="column-bar column-bar--left"></div>
      <div class="column-bar column-bar--right">
        <h2 class="section-title">Who we are?</h2>
      </div>

      <div class="text-column text-column--left">
        <h3 class="column-subhead">What we offer</h3>
        <p class="column-copy">Executive search, contract staffing, temp-to-hire and direct placement services for growing teams in finance, healthcare, technology, manufacturing and more.</p>
        <p class="column-copy">Every client works with one dedicated recruiter who answers quickly and keeps the process clear.</p>
      </div>

      <div class="text-column text-column--right">
        <h3 class="column-subhead">Executive search partners</h3>
        <p class="column-copy">We are a full service executive recruiting and staffing company working within all vertical markets across the United States. Our consultants learn each client's culture, goals and hiring needs before a single résumé is shared.</p>
        <p class="column-copy">From temporary support to senior leadership searches, we screen every candidate carefully and follow each placement through the first months on the job.</p>
      </div>

      <div class="accent-band"></div>

      <div class="contact-panel">
        <ul class="contact-list">
          <li><a href="mailto:info@brambletonhiregroup.example">info@brambletonhiregroup.example</a></li>
          <li><a href="https://www.brambletonhiregroup.example">www.brambletonhiregroup.example</a></li>
        </ul>
      </div>
    </section>
  </div>
</body>
</html>
```